Book Cover: A Quiet Cartographer

DO NOT JUST COPY THE BOOK COVER I HAVE ADDED FOR REFERENCE. I NEED SOMETHING FRESH NOT JUST A COPY AND PASTE!
If you cannot improve on the design with something creative then don't submit a design.

Project Title:
Book Cover Design for A Quiet Cartographer

Must be better than the mock design I have uploaded in project files.

Project Description:
I’m looking for a striking and emotionally evocative book cover for my upcoming title A Quiet Cartographer. This is a deeply personal and powerful memoir about the masks we wear, emotional survival, control, and the journey toward radical self-awareness and healing. The cover should visually represent the contrast between the performative self and the authentic self.

Visual Concept:
Please take visual inspiration and design continuity from my previous book Run FAR Now! — I will upload that cover for reference. This new design should feel like a continuation of the same author journey, but bolder and more psychologically intense.

You’ll be provided with two photos of me:

One where I appear more unkept, raw, and emotionally heavy.

One where I appear clean, centered, and lighter.

These can either be:

Split down the middle to create a “mirror” or duality effect (symbolizing the split self),

Or placed side by side as a subtle before/after or internal/external representation.

You may also consider overlaying or fading one into the other if done tastefully.

The mood should hint at internal conflict, self-reckoning, and healing—but without looking too “self-help cliché.” Think masculine, introspective, modern, and editorial. Avoid overly bright or busy visuals. A minimal or clean design with strong type hierarchy is preferred.

Key Themes to Represent Visually (even abstractly):

Narcissism as a survival mechanism

The emotional cost of performance

The tension between image and authenticity

The healing journey from ego to empathy

Design References:

Run FAR Now! (uploaded) — continuity of brand and typography encouraged

Memoir-style covers like Lanterns Along the Winter Harbour, Saltwater, or A Kettle Hums at Dusk for layout feel

If using color, muted tones with contrast (black/white, sepia, desaturated blues or greys) work well

Title: A Quiet Cartographer
Subtitle (optional placement): Not every narcissist is a monster. Some are just wounded men trying their best to survive
Author: Marlon Weskett

Deliverables:

Full front cover for print sale size as previous cover, including space for subtitle and author name

Spine and back cover (leave placeholder text if no blurb is given)

Ebook cover version

High-resolution files suitable for Quillmark QPS and print use

Additional Notes:
Please ensure the tone stays emotionally resonant, masculine, and sophisticated. No stock image models or cliché therapist symbols. Use my uploaded photos only.

Looking forward to seeing your vision come to life.

Back Cover Blurb – A Quiet Cartographer
A brutally honest recovery story—about what happens after you get clean, and the ego you still have to face.
Most people think addiction ends when you put down the drink, the drug, or the chaos.
But for Marlon Weskett, sobriety was just the start.
Behind the personal development posts, six-pack selfies, and billion-rand property deals, he was still chasing the one thing rehab never took from him: the need to be admired.
This book is not a confession. It’s a dismantling.
In A Quiet Cartographer, Marlon exposes the hidden patterns of ego, control, and validation-seeking that nearly cost him everything—even after he got “better.” With fearless self-inquiry and raw storytelling, he invites readers into his recovery from performance, perfectionism, and power addiction.
Whether you’ve been the narcissist—or you’ve loved one—this book is a mirror. And what you’ll find is not just insight, but a new path forward: one where truth is more powerful than charm, and safety matters more than being impressive.
This isn’t about being perfect.
It’s about being honest.
And finally becoming someone worth trusting—especially by yourself.

Target Market(s)

Any reader wanting to read about narcissism and love

Font styles to use
Sans Serif

Colors
EB3D1F
EC4F4E
F09395
F8D3D4
FCEDEE

Requirements
Must have
• Must be better than the mock design I uploaded.

```html
<!DOCTYPE html>
<html lang="en">
<head>
<meta charset="utf-8">
<title>A Quiet Cartographer — Marlon Weskett</title>
<link rel="stylesheet" href="https://fonts.googleapis.com/css2?family=Anton&family=Montserrat:wght@500;600;800&family=Oswald:wght@500;600&display=swap">
<style>
  :root {
    --ground: #1c1b1d;
    --ground-soft: #29272a;
    --flame: #eb3d1f;
    --coral: #ec4f4e;
    --rose: #f09395;
    --blush: #f8d3d4;
    --shell: #fcedee;
    --heavy-top: #5b504c;
    --heavy-bottom: #2f2a29;
    --light-top: #d9b3a6;
    --light-bottom: #a9837a;
  }
  html, body {
    margin: 0;
    padding: 0;
    width: 846px;
    height: 1200px;
    overflow: hidden;
    background: var(--ground);
  }
  .cover {
    position: relative;
    width: 846px;
    height: 1200px;
    overflow: hidden;
  }
  .cover svg { display: block; }
  .endorsement {
    font-family: "Montserrat", sans-serif;
    font-weight: 500;
    font-size: 14px;
    fill: var(--blush);
    text-anchor: middle;
  }
  .endorser {
    font-family: "Montserrat", sans-serif;
    font-weight: 800;
    font-size: 12px;
    letter-spacing: 3px;
    fill: var(--rose);
    text-anchor: middle;
  }
  .title-small {
    font-family: "Anton", sans-serif;
    font-size: 64px;
    letter-spacing: 6px;
    fill: var(--shell);
  }
  .title-accent { fill: var(--coral); }
  .title-large {
    font-family: "Anton", sans-serif;
    font-size: 122px;
    fill: var(--shell);
  }
  .subtitle {
    font-family: "Montserrat", sans-serif;
    font-weight: 600;
    font-size: 18px;
    fill: var(--blush);
    text-anchor: middle;
  }
  .author {
    font-family: "Oswald", sans-serif;
    font-weight: 600;
    font-size: 28px;
    letter-spacing: 12px;
    fill: var(--shell);
    text-anchor: middle;
  }
</style>
</head>
<body>
<main class="cover">
  <svg width="846" height="1200" viewBox="0 0 846 1200" xmlns="http://www.w3.org/2000/svg">
    <defs>
      <radialGradient id="ground-glow" cx="0.5" cy="0.35" r="0.8">
        <stop offset="0" stop-color="var(--ground-soft)"/>
        <stop offset="1" stop-color="var(--ground)"/>
      </radialGradient>
      <linearGradient id="self-heavy" x1="0" y1="0" x2="0" y2="1">
        <stop offset="0" stop-color="var(--heavy-top)"/>
        <stop offset="1" stop-color="var(--heavy-bottom)"/>
      </linearGradient>
      <linearGradient id="self-light" x1="0" y1="0" x2="0" y2="1">
        <stop offset="0" stop-color="var(--light-top)"/>
        <stop offset="1" stop-color="var(--light-bottom)"/>
      </linearGradient>
    </defs>

    <rect class="backdrop" width="846" height="1200" fill="url(#ground-glow)"/>

    <!-- endorsement -->
    <g class="endorsement-block">
      <text class="endorsement" x="423" y="52">“Whatever we’ve been through, Marlon not only makes us feel</text>
      <text class="endorsement" x="423" y="72">we can get over it, he gives us the tools to do exactly that.”</text>
      <text class="endorser" x="423" y="98">CALLUM ASHBY</text>
    </g>

    <!-- split portrait: the raw self and the performed self -->
    <g class="portrait-split">
      <polygon role="img" aria-label="Author portrait, left half: bearded, unkempt, emotionally heavy, desaturated"
               points="70,130 446,130 428,260 458,380 414,500 440,610 420,720 70,720"
               fill="url(#self-heavy)"/>
      <polygon role="img" aria-label="Author portrait, right half: clean-shaven, centred, lighter, warm tones"
               points="458,130 776,130 776,720 432,720 452,610 426,500 470,380 440,260"
               fill="url(#self-light)"/>
      <!-- fracture line -->
      <polyline points="452,118 434,260 464,380 420,500 446,610 426,732"
                fill="none" stroke="var(--flame)" stroke-width="3"/>
      <!-- shard slivers drifting off the crack -->
      <polygon points="474,392 520,372 486,404" fill="var(--coral)"/>
      <polygon points="404,506 362,528 398,516" fill="var(--rose)"/>
      <polygon points="458,612 500,632 462,620" fill="var(--blush)"/>
    </g>

    <!-- title -->
    <g class="title">
      <text class="title-small" x="70" y="806">A <tspan class="title-accent">QUIET</tspan></text>
      <text class="title-large" x="70" y="926" textLength="706" lengthAdjust="spacingAndGlyphs">CARTOGRAPHER</text>
    </g>

    <!-- subtitle -->
    <g class="subtitle-block">
      <rect x="70" y="950" width="706" height="3" fill="var(--flame)"/>
      <text class="subtitle" x="423" y="990">Not every narcissist is a monster. Some are just</text>
      <text class="subtitle" x="423" y="1016">wounded men trying their best to survive</text>
    </g>

    <!-- author -->
    <g class="author-block">
      <rect x="417" y="1068" width="12" height="12" fill="var(--coral)"/>
      <text class="author" x="429" y="1140">MARLON WESKETT</text>
    </g>
  </svg>
</main>
</body>
</html>
```